Cruise Booking Website

Cruise search and booking website

This project is a redesign of a cruise booking website we did a few years ago.

The current website is located here: http://voyage.pixelmarsh.com/en/

It's not fully functional but gives you ad idea how miserable the old design was.

All the information about cruises, cruise lines, destinations, ports and shore excursions will be similar to http://www.sailorbay.com/
Actual search pages (form, results, single result, sailing and cabin selection, ship info, booking) will have EXACTLY the same info as sailorbay.com

We like the style of http://harborvoyagehub.com, it's quite modern, good spacing, not overloaded with information. So you can use it as an example of what we like, not what we want as a final result for us. Please, don't copy it. The result should not be possible to resemble the harborvoyagehub.com, because our site has to be unique. This is important!
If you submit a design that clearly reminds another cruise site it will be rejected!

Also the mockup provided is just to give you the basic structure and show what information has to be present on the page. It doesn't mean the layout has to be the same as a mockup. The layout is up to the designer.

I've updated the mockup to be more generic so it doesn't confuse you:
https://www.filecrate.net/s/k7q2mz9pw4tnb3x/Home%20page.png

When you're adding social sharing icons like chatterbox/peeplet you have to use chinese ones instead:
https://www.filecrate.net/s/h3rt8wyd6jcl0fe/chinese-social-icons.png
Originals: http://shrtlk.example/qRmT

We'll start with home page first and after it's approved inner pages can be designed.

I know the cost of the project doesn't look high, but the task is straight forward and doesn't require to be very original, it's better to follow existing design and layout patterns that proved to work well.
That's why I encourage you to choose a template to build the design on top of one of https://themequarry.net/ themes if it will save the design work, will be easier and faster for you. So it will be more like a customization than a new design from scratch.

Mockups, site map and logo files:
- https://www.filecrate.net/sh/50xb7vq1ndtpkez/RmwuHp8Zq3

Website tree:
- https://papers.quillnet.example/document/d/8vTrXk2MqLpZ4wNsB7yHcE1oUjFgD9aR_QbVtnWm/edit?usp=sharing
Updates

So far a lot of designs are just copying http://www.harborvoyagehub.com/ - we don't like it!

We like the style of harborvoyagehub.com, it's quite modern, good spacing, not overloaded with information. So you can use it as an example of what we like, not what we want as a final result for us. Please, don't copy it. The result should not be possible to resemble the harborvoyagehub.com, because our site has to be unique. This is important!

Target Market(s)

Chinese travellers

Industry/Entity Type

Build

Requirements
Must have
• * White, blue and red
* Large spacing, not too much information cramped into a small space like sailorbay.com or the current website
* More "hidden" info in popups, tabs and so on, so not to many things are visible at the same time
* Compatible with lumen framekit styling (for easier coding):
- http://lumenkit.example.io/framework/index.html
- http://skinvault.net/
* Feel free to propose to build the design on top of one of https://themequarry.net/ themes if it will save the design work, will be easier and faster for you

```html
<!DOCTYPE html>
<html lang="en">
<head>
<meta charset="utf-8">
<title>Haiyun Cruises – Cruise Booking</title>
<link href="https://fonts.googleapis.com/css2?family=Alegreya+Sans+SC:wght@400;500;700;800&family=Raleway:wght@400;500;700&family=Open+Sans:wght@400;600&display=swap" rel="stylesheet">
<style>
  :root {
    --blue: #2f6fa8;
    --blue-dark: #255c8f;
    --blue-text: #2a6aa6;
    --red: #d62b2b;
    --red-dark: #b81f1f;
    --ink: #444;
    --muted: #7a7a7a;
    --line: #d9d9d9;
    --white: #fff;
    --sky-top: #f2f6fa;
    --sky-mid: #c9dcec;
  }
  * { box-sizing: border-box; margin: 0; padding: 0; }
  html, body { width: 1088px; height: 1200px; overflow: hidden; background: var(--white); }
  body { position: relative; font-family: "Open Sans", sans-serif; color: var(--ink); }
  .sc { font-family: "Alegreya Sans SC", sans-serif; }

  /* Hero */
  .hero {
    position: absolute; left: 0; top: 0; width: 1088px; height: 300px;
    background: linear-gradient(180deg, var(--sky-top) 0%, #e3edf5 45%, var(--sky-mid) 100%);
  }
  .hero-scene {
    position: absolute; left: 0; top: 0; width: 1088px; height: 300px;
    background:
      radial-gradient(ellipse 220px 180px at 80px 190px, rgba(120,160,120,.35), transparent 70%),
      radial-gradient(ellipse 340px 120px at 820px 230px, rgba(255,255,255,.95), transparent 70%),
      radial-gradient(ellipse 300px 160px at 330px 200px, rgba(255,255,255,.8), transparent 70%),
      linear-gradient(180deg, rgba(255,255,255,.6), rgba(180,205,225,.4));
  }
  .topbar {
    position: absolute; left: 182px; top: 0; width: 724px; height: 56px;
    border-bottom: 1px dotted #c8c8c8;
  }
  .phone { position: absolute; left: 4px; top: 28px; display: flex; align-items: center; gap: 6px;
    font-family: "Raleway", sans-serif; font-size: 12px; color: #333; }
  .phone strong { color: var(--blue-text); font-size: 14px; font-style: italic; font-weight: 700; margin-left: 6px; }
  .account { position: absolute; right: 4px; top: 10px; display: flex; gap: 12px; font-size: 13px; color: var(--blue-text); }
  .account a { color: inherit; text-decoration: none; display: flex; flex-direction: column; align-items: center; gap: 1px; }
  .account .sep { color: #bbb; align-self: flex-end; }
  .tagline { position: absolute; left: 524px; top: 76px; font-family: "Raleway", sans-serif; line-height: 1; }
  .tagline .l1 { font-size: 20px; color: var(--blue-text); font-weight: 500; }
  .tagline .l2 { font-size: 23px; color: #222; font-weight: 500; margin-top: 4px; }
  .tagline .l2 b { color: var(--red); font-weight: 700; }
  .brand-disc {
    position: absolute; left: 435px; top: 140px; width: 220px; height: 220px; border-radius: 50%;
    background: var(--white); display: flex; flex-direction: column; align-items: center; padding-top: 66px;
  }
  .brand-disc .mark { width: 14px; height: 14px; border-radius: 50%; background: var(--blue); margin-bottom: 10px; }
  .brand-disc .name { font-family: "Raleway", sans-serif; font-weight: 700; font-size: 26px; color: var(--blue-dark); }
  .brand-disc .url { font-family: "Raleway", sans-serif; font-weight: 700; font-size: 10px; color: var(--blue-dark); margin-top: 4px; }

  /* Navigation */
  .main-nav {
    position: absolute; left: 0; top: 300px; width: 1088px; height: 38px; background: var(--blue);
    display: flex; justify-content: center; align-items: center;
  }
  .main-nav a { color: var(--white); text-decoration: none; font-size: 16px; padding: 0 12px; position: relative; }
  .main-nav a + a::before { content: ""; position: absolute; left: 0; top: 5px; height: 11px; border-left: 1px dotted rgba(255,255,255,.6); }

  /* Search */
  .search-title { position: absolute; top: 344px; left: 0; width: 1088px; text-align: center;
    font-size: 46px; font-weight: 800; color: var(--red); line-height: 1; }
  .filters { position: absolute; left: 200px; top: 398px; display: flex; gap: 8px; }
  .select {
    width: 168px; height: 29px; border: 1px solid #cfcfcf; border-radius: 3px; background: var(--white);
    box-shadow: 0 1px 2px rgba(0,0,0,.12); display: flex; align-items: center; justify-content: space-between;
    padding: 0 12px; font-size: 14px; color: #333;
  }
  .select::after { content: ""; border: 6px solid transparent; border-top: 6px solid #222; border-bottom: 0; }
  .routes-note { position: absolute; left: 201px; top: 438px; font-size: 18px; color: var(--blue-text); }
  .advanced { position: absolute; left: 661px; top: 443px; font-size: 16px; color: var(--blue-text); text-decoration: underline; }
  .btn-red { background: var(--red); color: var(--white); border-radius: 3px; display: flex; align-items: center; justify-content: center; }
  .search-btn { position: absolute; left: 781px; top: 434px; width: 108px; height: 34px; font-size: 20px; }
  .section-rule { position: absolute; left: 0; top: 482px; width: 1088px; height: 2px; background: #cfcfcf; box-shadow: 0 1px 3px rgba(0,0,0,.12); }

  /* About */
  .about-title { position: absolute; left: 199px; top: 498px; font-size: 40px; font-weight: 800; color: var(--blue-dark); line-height: 1; }
  .about-copy { position: absolute; left: 200px; top: 548px; width: 362px; font-size: 8.4px; line-height: 1.55; color: #555; }
  .about-copy p + p { margin-top: 10px; }
  .video { position: absolute; left: 574px; top: 550px; width: 326px; height: 265px; border: 4px solid #c9c9c9; background: #222; }
  .video-still { width: 100%; height: 237px; background: linear-gradient(180deg, #4d86c8 0%, #86b2dc 55%, #dfe7ee 70%, #5d7f9c 100%); }
  .video-bar { height: 20px; background: #111; display: flex; align-items: center; gap: 10px; padding: 0 10px; color: #ddd; font-size: 7px; position: relative; }
  .video-bar::before { content: ""; position: absolute; left: 0; top: -2px; width: 60px; height: 2px; background: var(--red); }
  .video-bar .ctl { width: 7px; height: 8px; border-left: 2px solid #ddd; border-right: 2px solid #ddd; }
  .video-bar .right { margin-left: auto; display: flex; gap: 8px; }
  .video-bar .right i { width: 9px; height: 7px; border: 1px solid #ddd; display: block; }

  /* Newsletter */
  .newsletter { position: absolute; left: 182px; top: 842px; width: 724px; height: 58px; background: var(--blue); }
  .newsletter h2 { position: absolute; left: 18px; top: 6px; font-size: 26px; font-weight: 700; color: var(--white); line-height: 1; }
  .newsletter p { position: absolute; left: 67px; top: 33px; font-size: 14px; color: var(--white); }
  .email-field { position: absolute; left: 304px; top: 16px; width: 284px; height: 28px; background: var(--white); border-radius: 3px;
    font-size: 14px; color: #444; padding: 5px 12px; }
  .subscribe { position: absolute; left: 600px; top: 17px; width: 108px; height: 28px; font-size: 20px; }

  /* Deals & partners */
  .block-head { position: absolute; top: 922px; display: flex; align-items: center; }
  .block-head h3 { font-size: 24px; font-weight: 700; color: var(--red); white-space: nowrap; line-height: 1; }
  .block-head .rule { flex: 1; border-top: 1px dotted #c8c8c8; margin: 0 8px 0 10px; }
  .arrows { display: flex; gap: 3px; }
  .arrows i { width: 17px; height: 17px; background: #ccc; display: flex; align-items: center; justify-content: center; }
  .arrows i::after { content: ""; border: 4px solid transparent; }
  .arrows i.prev::after { border-right: 5px solid var(--white); border-left: 0; }
  .arrows i.next::after { border-left: 5px solid var(--white); border-right: 0; }
  .deals-head { left: 200px; width: 441px; }
  .partners-head { left: 666px; width: 234px; }
  .deal { position: absolute; top: 962px; width: 141px; height: 156px; }
  .deal .photo { height: 126px; position: relative; }
  .deal .caption { position: absolute; left: 0; bottom: 0; width: 100%; height: 37px; background: rgba(30,30,30,.72);
    color: var(--white); font-size: 12.5px; line-height: 1.15; padding: 3px 9px; }
  .deal .price { height: 30px; background: var(--blue); color: var(--white); font-size: 14px; padding: 6px 9px; }
  .partner-box { position: absolute; left: 664px; top: 962px; width: 236px; height: 157px; border: 1px solid #dadada;
    display: flex; flex-direction: column; align-items: center; justify-content: center; gap: 6px; }
  .partner-box .name { font-family: "Raleway", sans-serif; font-size: 30px; font-weight: 700; color: var(--blue-dark); }
  .partner-box .sub { font-family: "Raleway", sans-serif; font-size: 8px; letter-spacing: 1.5px; color: var(--blue-dark); }

  /* Footer */
  .footer-rule { position: absolute; left: 0; top: 1147px; width: 1088px; height: 2px; background: #cfcfcf; }
  .copyright { position: absolute; left: 204px; top: 1166px; font-size: 12px; color: #9a9a9a; }
  .share { position: absolute; left: 768px; top: 1164px; display: flex; gap: 5px; }
  .share i { width: 17px; height: 17px; border-radius: 3px; display: block; }
</style>
</head>
<body>

<header class="hero">
  <div class="hero-scene" role="img" aria-label="Tropical sky with palm tree, mountain and a large white cruise ship"></div>
  <div class="topbar">
    <div class="phone">
      <svg width="16" height="16" viewBox="0 0 24 24"><path fill="#d62b2b" d="M6.6 10.8a15 15 0 0 0 6.6 6.6l2.2-2.2c.3-.3.7-.4 1-.2 1.1.4 2.3.6 3.6.6.6 0 1 .4 1 1V20c0 .6-.4 1-1 1A17 17 0 0 1 3 4c0-.6.4-1 1-1h3.5c.6 0 1 .4 1 1 0 1.3.2 2.5.6 3.6.1.3 0 .7-.2 1z"/></svg>
      Call us today! <strong>4008 512 309</strong>
    </div>
    <nav class="account sc">
      <a href="#"><svg width="14" height="16" viewBox="0 0 14 16"><rect x="1" y="7" width="12" height="9" rx="1.5" fill="#d62b2b"/><path d="M3.5 7V5a3.5 3.5 0 0 1 7 0v2" fill="none" stroke="#d62b2b" stroke-width="2"/></svg>Sign Up</a>
      <span class="sep">⋮</span>
      <a href="#"><svg width="16" height="16" viewBox="0 0 16 16"><circle cx="11" cy="5" r="4" fill="none" stroke="#d62b2b" stroke-width="2"/><path d="M8 8 2 14M4 12l2 2" stroke="#d62b2b" stroke-width="2"/></svg>Sign In</a>
    </nav>
  </div>
  <div class="tagline">
    <div class="l1">WE ’RE THE MOST ADVANCED</div>
    <div class="l2"><b>CRUISE BOOKING</b> PROVIDER IN <b>CHINA</b></div>
  </div>
  <div class="brand-disc">
    <span class="mark"></span>
    <span class="name">Haiyun Cruises</span>
    <span class="url">www.haiyuncruise.com</span>
  </div>
</header>

<nav class="main-nav sc">
  <a href="#">Home</a><a href="#">Destinations</a><a href="#">Cruise Lines</a><a href="#">Cruise Info</a><a href="#">Deals</a><a href="#">OnlineBooking</a><a href="#">Contact Us</a><a href="#">Blog</a><a href="#">Search</a>
</nav>

<section class="search">
  <h1 class="search-title sc">Search Cruises</h1>
  <div class="filters sc">
    <div class="select">Asia</div>
    <div class="select">July 2013</div>
    <div class="select">Any Length</div>
    <div class="select">Any Cruise Line</div>
  </div>
  <div class="routes-note sc">More than 10,000 routes for you</div>
  <a class="advanced sc" href="#">Advanced Search</a>
  <div class="search-btn btn-red sc">Search</div>
</section>
<div class="section-rule"></div>

<section class="about">
  <h2 class="about-title sc">about us</h2>
  <div class="about-copy">
    <p>Lorem ipsum dolor sit amet, consectetuer adipiscing elit, sed diam nonummy nibh euismod tincidunt ut laoreet dolore magna aliquam erat volutpat. Ut wisi enim ad minim veniam, quis nostrud exerci tation ullamcorper suscipit lobortis nisl ut aliquip ex ea commodo consequat.</p>
    <p>Duis autem vel eum iriure dolor in hendrerit in vulputate velit esse molestie consequat, vel illum dolore eu feugiat nulla facilisis at vero eros et accumsan et iusto odio dignissim qui blandit praesent luptatum zzril delenit augue duis dolore te feugait nulla facilisi.</p>
    <p>Sed diam nonummy nibh euismod tincidunt ut laoreet dolore magna aliquam erat volutpat. Ut wisi enim ad minim veniam, quis nostrud exerci tation ullamcorper suscipit lobortis nisl ut aliquip ex ea commodo consequat.</p>
    <p>Vel eum iriure dolor in hendrerit in vulputate velit esse molestie consequat, vel illum dolore eu feugiat nulla facilisis at vero eros et accumsan et iusto odio dignissim qui blandit praesent luptatum zzril delenit augue duis dolore te feugait nulla facilisi. Ut wisi enim ad minim veniam, quis nostrud exerci tation ullamcorper suscipit lobortis nisl ut aliquip ex ea commodo consequat. Vel illum dolore eu feugiat nulla facilisis at vero eros et accumsan et iusto odio dignissim qui blandit praesent luptatum zzril delenit augue duis dolore te feugait nulla facilisi.</p>
  </div>
  <div class="video">
    <div class="video-still" role="img" aria-label="Video still: company founder holding an award in front of a cruise ship at sea"></div>
    <div class="video-bar">
      <span class="ctl"></span><span>◀)</span><span>02:54 / 12:45</span>
      <span class="right"><i></i><i></i><i></i></span>
    </div>
  </div>
</section>

<section class="newsletter sc">
  <h2>Cruise Deals Newsletter</h2>
  <p>Subscribe to the best cruise deals now!</p>
  <div class="email-field">Enter Your Email Address</div>
  <div class="subscribe btn-red">Subscribe</div>
</section>

<div class="block-head deals-head sc"><h3>Last Minute Deals</h3><span class="rule"></span><span class="arrows"><i class="prev"></i><i class="next"></i></span></div>
<div class="block-head partners-head sc"><h3>Our Partners</h3><span class="rule"></span><span class="arrows"><i class="prev"></i><i class="next"></i></span></div>

<article class="deal sc" style="left:199px">
  <div class="photo" role="img" aria-label="Cruise ship below snowy Alaskan mountains" style="background:linear-gradient(180deg,#8a97a6,#dfe4ea 45%,#6d7f92)">
    <div class="caption">Alaska Cruises<br>7 Days From Whittier</div>
  </div>
  <div class="price">From $ 249</div>
</article>
<article class="deal sc" style="left:350px">
  <div class="photo" role="img" aria-label="Couple relaxing on a cruise ship deck" style="background:linear-gradient(180deg,#dfe6ea,#c8a47a 55%,#6f8aa0)">
    <div class="caption">Bermuda<br>7 Days From Whittier</div>
  </div>
  <div class="price">From $ 649</div>
</article>
<article class="deal sc" style="left:499px">
  <div class="photo" role="img" aria-label="Cruise ship docked at a Baltic harbour town" style="background:linear-gradient(180deg,#b9c8d8,#e7ecef 50%,#5f7386)">
    <div class="caption">Baltic cruises</div>
  </div>
  <div class="price">From $ 799</div>
</article>

<div class="partner-box">
  <span class="name">Marisol Lines</span>
  <span class="sub">CRUISE PARTNER</span>
</div>

<div class="footer-rule"></div>
<footer>
  <div class="copyright sc">© 2013 haiyuncruise.com. All rights reserved.</div>
  <div class="share" aria-label="Share">
    <i style="background:#3d8fd6"></i><i style="background:#e2352b"></i><i style="background:#2fa3e0"></i><i style="background:#4a78c2"></i><i style="background:#f08a24"></i><i style="background:#5bb834"></i>
  </div>
</footer>

</body>
</html>
```